Flyer desing for our garden union

Hello please design an flyer for our Garden /Union for our annual open day.
Please add fruit,vegtables and pukins and gardening stuff on it.

Colors

Designer to choose colors to be used in the design.

Requirements
Must have
• The name is : Volkstuin Vereniging De Zonnehoek
• Please add the following tekst: Open Dag op Zondag 22 September 11:00 - 16:00
• Website: www.vtvdezonnehoek-fictief.nl
• adres:Bremakkerlaan 12, 8219 KT Lelystad
Nice to have
• cotton candy and bouncer for the kids

```html
<!DOCTYPE html>
<html lang="nl">
<head>
<meta charset="utf-8">
<title>Open Dag – Volkstuin Vereniging De Zonnehoek</title>
<link rel="stylesheet" href="https://fonts.googleapis.com/css2?family=Montserrat:wght@400;500;700&display=swap">
<style>
  :root {
    --page-bg: #e6e6e6;
    --flyer-bg: #070707;
    --ink: #ffffff;
    --placeholder: #2b2b2b;
    --placeholder-edge: #4a4a4a;
    --fruit-a: #e9c53a;
    --fruit-b: #d9323c;
    --fruit-c: #a8c64a;
    --greens: #3f7a2c;
    --pumpkin-a: #f08a1c;
    --pumpkin-b: #d85f0c;
    --line: #d9d9d9;
  }
  * { margin: 0; padding: 0; box-sizing: border-box; }
  html, body { width: 1200px; height: 1080px; overflow: hidden; }
  body {
    background: var(--page-bg);
    font-family: "Montserrat", sans-serif;
    color: var(--ink);
  }
  .flyer {
    position: absolute;
    left: 250px; top: 45px;
    width: 700px; height: 990px;
    background: var(--flyer-bg);
    overflow: hidden;
    box-shadow: 0 18px 40px rgba(0,0,0,0.25);
  }
  .flyer-art { position: absolute; inset: 0; }
  .club-name {
    position: absolute;
    left: 90px; top: 580px;
    font-size: 40px; font-weight: 400;
    line-height: 46px;
    letter-spacing: 0.5px;
  }
  .event-title {
    position: absolute;
    left: 75px; top: 724px;
    font-size: 52px; font-weight: 700;
    letter-spacing: 0.5px;
    white-space: nowrap;
  }
  .event-date {
    position: absolute;
    left: 165px; top: 800px;
    font-size: 30px; font-weight: 400;
    letter-spacing: 0.5px;
    white-space: nowrap;
  }
  .footer {
    position: absolute;
    left: 40px; right: 30px; top: 860px;
    border-top: 2px solid var(--line);
    display: flex; align-items: center;
    padding-top: 26px;
    font-size: 13px; font-weight: 500;
    white-space: nowrap;
  }
  .footer-item { display: flex; align-items: center; gap: 10px; }
  .footer-divider {
    width: 2px; height: 46px; background: var(--line);
    margin: 0 14px;
  }
  .footer svg { flex: none; }
</style>
</head>
<body>
  <div class="flyer">
    <svg class="flyer-art" width="700" height="990" viewBox="0 0 700 990">
      <defs>
        <radialGradient id="fruitTones" cx="0.4" cy="0.45" r="0.7">
          <stop offset="0" stop-color="var(--fruit-c)"/>
          <stop offset="0.55" stop-color="var(--fruit-a)"/>
          <stop offset="1" stop-color="var(--fruit-b)"/>
        </radialGradient>
        <radialGradient id="pumpkinTones" cx="0.5" cy="0.5" r="0.6">
          <stop offset="0" stop-color="var(--pumpkin-a)"/>
          <stop offset="1" stop-color="var(--pumpkin-b)"/>
        </radialGradient>
      </defs>
      <path class="divider-curve" d="M0 440 Q140 470 270 420" fill="none" stroke="var(--ink)" stroke-width="6"/>
      <rect class="gardener-art" x="55" y="70" width="190" height="280" rx="12" fill="var(--placeholder)" role="img" aria-label="Illustratie van een tuinman met hark en gieter"/>
      <circle class="photo-fruit" cx="520" cy="150" r="250" fill="url(#fruitTones)" stroke="var(--ink)" stroke-width="8" role="img" aria-label="Foto van druiven, frambozen, appels en sinaasappels"/>
      <circle class="photo-greens" cx="215" cy="430" r="95" fill="var(--greens)" stroke="var(--ink)" stroke-width="7" role="img" aria-label="Foto van bladgroente"/>
      <circle class="photo-pumpkins" cx="405" cy="420" r="142" fill="url(#pumpkinTones)" stroke="var(--ink)" stroke-width="8" role="img" aria-label="Foto van oranje pompoenen"/>
      <rect class="pumpkin-art" x="574" y="466" width="88" height="58" rx="10" fill="var(--placeholder)" stroke="var(--placeholder-edge)" stroke-width="1.5" role="img" aria-label="Lijntekening van een kleine pompoen"/>
      <rect class="pumpkin-art" x="534" y="540" width="128" height="82" rx="12" fill="var(--placeholder)" stroke="var(--placeholder-edge)" stroke-width="1.5" role="img" aria-label="Lijntekening van een grote pompoen"/>
    </svg>

    <h1 class="club-name">Volkstuin<br>Vereniging<br>De Zonnehoek</h1>
    <p class="event-title">Open Dag op Zondag</p>
    <p class="event-date">22 September 11:00 - 16:00</p>

    <div class="footer">
      <div class="footer-item">
        <svg width="32" height="32" viewBox="0 0 40 40" fill="none" stroke="var(--ink)" stroke-width="2" aria-hidden="true">
          <circle cx="20" cy="20" r="17"/>
          <ellipse cx="20" cy="20" rx="8" ry="17"/>
          <path d="M3 20h34M6 11h28M6 29h28M20 3v34"/>
        </svg>
        <span>www.vtvdezonnehoek-fictief.nl</span>
      </div>
      <div class="footer-divider"></div>
      <div class="footer-item">
        <svg width="32" height="36" viewBox="0 0 40 44" fill="none" stroke="var(--ink)" stroke-width="2.5" aria-hidden="true">
          <path d="M20 32 C12 22 9 17 9 13 a11 11 0 0 1 22 0 c0 4 -3 9 -11 19z"/>
          <circle cx="20" cy="13" r="4"/>
          <ellipse cx="20" cy="36" rx="16" ry="5"/>
        </svg>
        <span>Bremakkerlaan 12, 8219 KT Lelystad</span>
      </div>
    </div>
  </div>
</body>
</html>
```